Book Cover for self help book describing how to become the author of your life

I need a good resolution front cover for a book that is published through Brelvox in Print and ebook format. I can design the spine and back cover myself so just need the front angle.
The book is titled "Paint Tomorrow Bright" and it's about writing your own story for how you want to live your life. The image I had in my mind was a pen writing out the title on the front in a script-like font, like actual handwriting.
I've included a very basic mock-up that I've done myself just to give the general idea. The cover requires three pieces of writing.
Title: Paint Tomorrow Bright
Subtitle: Walk Along the Quiet Harbour Path
Author: Martin Folwell
Female 35-55

```html
<!DOCTYPE html>
<html lang="en">
<head>
<meta charset="utf-8">
<title>Paint Tomorrow Bright — Front Cover</title>
<link href="https://fonts.googleapis.com/css2?family=Mrs+Saint+Delafield&display=swap" rel="stylesheet">
<style>
  :root {
    --page-bg: #ffffff;
    --paper-light: #f8efe7;
    --paper-mid: #f1e2d6;
    --paper-edge: #ead6c6;
    --ink: #1f1c1b;
    --skin-light: #e9c2a4;
    --skin-deep: #c99476;
  }
  * { margin: 0; padding: 0; box-sizing: border-box; }
  html, body {
    width: 1200px;
    height: 1200px;
    overflow: hidden;
    background: var(--page-bg);
  }
  .canvas {
    position: relative;
    width: 1200px;
    height: 1200px;
  }
  .cover {
    position: absolute;
    left: 220px;
    top: 28px;
    width: 760px;
    height: 1144px;
    overflow: hidden;
    background: radial-gradient(ellipse at 50% 60%, var(--paper-light) 0%, var(--paper-mid) 60%, var(--paper-edge) 100%);
    font-family: "Mrs Saint Delafield", cursive;
    color: var(--ink);
  }
  .title {
    position: absolute;
    left: 0;
    right: 0;
    top: 120px;
    text-align: center;
    font-weight: 400;
    font-size: 168px;
    line-height: 0.95;
  }
  .title-line { display: block; }
  .subtitle {
    position: absolute;
    left: 0;
    right: 0;
    top: 640px;
    text-align: center;
    font-weight: 400;
    font-size: 88px;
    line-height: 0.95;
  }
  .subtitle-line { display: block; }
  .author {
    position: absolute;
    left: 160px;
    top: 905px;
    font-size: 70px;
    line-height: 1;
    white-space: nowrap;
  }
  .hand-pencil {
    position: absolute;
    left: 560px;
    top: 900px;
    width: 200px;
    height: 244px;
    border-top-left-radius: 120px 140px;
    background: radial-gradient(ellipse at 70% 55%, var(--skin-light) 0%, var(--skin-deep) 70%, rgba(201,148,118,0) 100%);
  }
</style>
</head>
<body>
<main class="canvas">
  <section class="cover">
    <h1 class="title">
      <span class="title-line">Paint Tomorrow</span>
      <span class="title-line">Bright</span>
    </h1>
    <h2 class="subtitle">
      <span class="subtitle-line">Walk Along the Quiet</span>
      <span class="subtitle-line">Harbour Path</span>
    </h2>
    <p class="author">Martin Folwell</p>
    <div class="hand-pencil" role="img" aria-label="Photograph of a hand holding a pencil, writing the author's name"></div>
  </section>
</main>
</body>
</html>
```